Political sign design, fonts colors and layout

I am running for Town Council.

My message is done, and *a draft is attached* with the text we wish to use. It says "Elect Dana Velmont" etc. In Maroon and White. I am not a designer, but this is somewhat close to what we are looking for.

I need help with colors and fonts, layout, spacing, and general cleanup.

I'm attaching the town high school logo:

- "H" for Brookfield: with black and white outlines on the fonts
- we want to incorporate the black and white on the fonts
- for the entire text, parts of the text, or best would be a mix

This is for signs printed and placed all over my town.

We need two versions

1. square, 4' by 4' version
2. 36" by 24" version

The smaller version will drop the three bullet pointed text, but otherwise can be identical.

The sign can only use 3 printed colors (due to printing costs.)

1. maroon,
2. white,
3. black.

The maroon should match the maroon from the high school logo attached, which I believe I did in the draft.

We also like the white border around the outside, like in the "scoreboard" design attached.

Thanks for your attention, wish me luck.

Dana

Target Market(s)

SIgns, Political market

Industry/Entity Type

Political

Font styles to use
Sans Serif
Other font styles liked:
• Arial Black, Sans Serif Bold

Requirements
Must have
• maroon background, white font.
• - black borders around fonts where appropriate
• - great spacing
• - great typeface usage
• - clean and crisp political sign, visible while driving.
• - my name "Dana Velmont" much larger like the draft, or the appropriate additional size
• - two versions, one square, and one 36" / 24"
Nice to have
• - nice borders
• - dress it up a bit, using italics and bold fonts, without making it flashy or busy.
Should not have
• Must be easily readable from a car, except for "Paid for by Friends of Dana Velmont" which can be tiny.
• Colors are noted in the description, the "Brookfield Maroon" as the background, white font, and some use of black.

```html
<!DOCTYPE html>
<html lang="en">
<head>
<meta charset="utf-8">
<title>Elect Dana Velmont – Yard Signs</title>
<link rel="stylesheet" href="https://fonts.googleapis.com/css2?family=Roboto:ital,wght@0,500;0,700;1,700;1,900&family=Roboto+Slab:wght@900&display=swap">
<style>
  :root {
    --maroon: #751c2e;
    --white: #ffffff;
    --black: #0b0b0b;
    --shadow: rgba(0, 0, 0, 0.35);
    --page: #ffffff;
  }
  html, body {
    margin: 0;
    width: 1200px;
    height: 1200px;
    overflow: hidden;
    background: var(--page);
  }
  .board { display: block; width: 1200px; height: 1200px; }
  .sign-face { fill: var(--maroon); }
  .sign-shadow { fill: var(--shadow); }
  .sign-frame { fill: none; stroke: var(--white); stroke-width: 2; }
  .vote-band { fill: var(--black); }
  .rule { stroke: var(--white); stroke-width: 2.5; }
  .star { fill: var(--white); }
  .tagline { font-family: "Roboto", Arial, sans-serif; font-style: italic; font-weight: 900; fill: var(--white); }
  .elect { font-family: "Roboto", Arial, sans-serif; font-weight: 500; fill: var(--white); }
  .candidate { font-family: "Roboto Slab", "Arial Black", serif; font-weight: 900; fill: var(--white); }
  .office { font-family: "Roboto", Arial, sans-serif; font-style: italic; font-weight: 700; fill: var(--white); }
  .issues { font-family: "Roboto", Arial, sans-serif; font-style: italic; font-weight: 700; fill: var(--white); letter-spacing: 1px; }
  .vote-call { font-family: "Roboto", Arial, sans-serif; font-weight: 700; fill: var(--white); }
  .website { font-family: "Roboto", Arial, sans-serif; font-weight: 700; fill: var(--white); letter-spacing: 6px; }
  .disclaimer { font-family: "Roboto", Arial, sans-serif; font-weight: 700; fill: var(--white); }
</style>
</head>
<body>
<svg class="board" viewBox="0 0 1500 1500" xmlns="http://www.w3.org/2000/svg" role="img" aria-label="Two campaign yard signs for Dana Velmont: square and wide versions">
  <defs>
    <polygon id="star" class="star" points="0,-27 5.9,-8.4 25.7,-8.3 9.6,3.2 15.9,21.8 0,10.4 -15.9,21.8 -9.6,3.2 -25.7,-8.3 -5.9,-8.4"/>
  </defs>

  <!-- Square sign -->
  <g class="sign sign--square">
    <rect class="sign-shadow" x="437" y="92" width="675" height="675"/>
    <rect class="sign-face" x="433" y="88" width="675" height="675"/>
    <path class="vote-band" d="M437 642 Q771 540 1104 642 L1104 759 L437 759 Z"/>
    <rect class="sign-frame" x="442" y="97" width="657" height="657"/>

    <text class="tagline" x="771" y="178" font-size="52" text-anchor="middle">Take back our town!</text>
    <text class="elect" x="478" y="245" font-size="34">Elect</text>
    <line class="rule" x1="577" y1="232" x2="876" y2="232"/>
    <use href="#star" x="934" y="228"/>
    <line class="rule" x1="980" y1="232" x2="1064" y2="232"/>

    <text class="candidate" x="771" y="395" font-size="178" text-anchor="middle">DANA</text>
    <text class="candidate" x="480" y="520" font-size="140" textLength="595" lengthAdjust="spacingAndGlyphs">VELMONT</text>

    <line class="rule" x1="483" y1="553" x2="697" y2="553"/>
    <text class="office" x="1071" y="560" font-size="22" text-anchor="end">for Brookfield Councilman/ Trustee</text>

    <text class="vote-call" x="776" y="678" font-size="46" text-anchor="middle">VOTE Nov 8th “Row A”</text>
    <text class="website" x="781" y="717" font-size="29" text-anchor="middle">www.votevelmont.com</text>
  </g>

  <!-- Wide sign -->
  <g class="sign sign--wide">
    <rect class="sign-shadow" x="335" y="829" width="876" height="582"/>
    <rect class="sign-face" x="331" y="825" width="876" height="582"/>
    <rect class="vote-band" x="335" y="1318" width="868" height="85"/>
    <rect class="sign-frame" x="338" y="832" width="862" height="568"/>

    <text class="tagline" x="768" y="872" font-size="37" text-anchor="middle">Take back our town!</text>
    <text class="elect" x="468" y="921" font-size="36">Elect</text>
    <line class="rule" x1="572" y1="907" x2="890" y2="907"/>
    <use href="#star" x="952" y="902"/>
    <line class="rule" x1="1000" y1="907" x2="1090" y2="907"/>

    <text class="candidate" x="780" y="1080" font-size="188" text-anchor="middle">DANA</text>
    <text class="candidate" x="470" y="1213" font-size="146" textLength="632" lengthAdjust="spacingAndGlyphs">VELMONT</text>

    <line class="rule" x1="473" y1="1247" x2="700" y2="1247"/>
    <text class="office" x="1097" y="1254" font-size="24" text-anchor="end">for Brookfield Councilman/ Trustee</text>

    <text class="issues" x="773" y="1299" font-size="20" text-anchor="middle">- Stop HIGH Taxes - Clean up Our Goverment - Preserve our Neighborhoods</text>

    <text class="vote-call" x="370" y="1375" font-size="42">VOTE Nov 8th “Row A”</text>
    <text class="website" x="1178" y="1360" font-size="27" text-anchor="end" style="letter-spacing:5px">www.votevelmont.com</text>
    <text class="disclaimer" x="1040" y="1378" font-size="16" text-anchor="middle">Paid for by Friends of Dana</text>
  </g>
</svg>
</body>
</html>
```